product development company PEVRANOX LLC business card

We need a business card design for a company based in Texas called 'PEVRANOX LLC'. Our first product is a illuminated portable ice chest that is called ' Ember Ridge coolers'. Ember ridge coolers is trademarked. I would like to have the ember ridge trademark somewhere on the card as well as the PEVRANOX LLC name.

Target Market(s)

outdoor industry

Industry/Entity Type

Business

Contact Information for Business Card

i would like to have PEVRANOX LLC logo larger than the Ember ridge coolers logo.

Font styles to use
Serif
Sans Serif

```html
<!DOCTYPE html>
<html lang="en">
<head>
<meta charset="utf-8">
<title>PEVRANOX LLC business card</title>
<link href="https://fonts.googleapis.com/css2?family=Montserrat:wght@400;500&family=Tinos:wght@400;700&display=swap" rel="stylesheet">
<style>
  :root {
    --page: #e9e6e1;
    --card-light: #f7f7f7;
    --card-light-edge: #dcdcdc;
    --card-dark: #1f1d1e;
    --card-dark-edge: #2d2a2b;
    --ink: #1c1c1c;
    --ink-soft: #6e6e6e;
    --ink-light: #f4f4f4;
    --icon: #b9b9b9;
  }
  * { margin: 0; padding: 0; box-sizing: border-box; }
  html, body { width: 1200px; height: 780px; overflow: hidden; }
  body {
    background: var(--page);
    position: relative;
    font-family: "Tinos", "Times New Roman", serif;
    color: var(--ink);
  }
  .card {
    position: absolute;
    top: 235px;
    width: 540px;
    height: 310px;
    border-radius: 4px;
    box-shadow: 0 14px 30px rgba(0,0,0,0.18);
    overflow: hidden;
  }
  .card--front {
    left: 40px;
    background: linear-gradient(135deg, var(--card-light) 0%, #ffffff 45%, var(--card-light-edge) 100%);
  }
  .card--back {
    left: 620px;
    background: linear-gradient(135deg, var(--card-dark-edge) 0%, var(--card-dark) 60%, #181617 100%);
  }

  /* company wordmark */
  .wordmark {
    position: absolute;
    font-family: "Montserrat", Arial, sans-serif;
    text-align: center;
  }
  .wordmark__name {
    font-weight: 500;
    letter-spacing: 6px;
    line-height: 1;
  }
  .wordmark__suffix {
    display: flex;
    align-items: center;
    justify-content: center;
    gap: 10px;
    margin-top: 8px;
    font-size: 15px;
    letter-spacing: 10px;
  }
  .wordmark__dots {
    flex: 1;
    border-top: 2px dotted currentColor;
  }
  .card--front .wordmark { left: 34px; top: 44px; width: 290px; color: var(--ink); }
  .card--front .wordmark__name { font-size: 38px; }
  .card--back .wordmark { left: 70px; top: 118px; width: 400px; color: var(--ink-light); }
  .card--back .wordmark__name { font-size: 52px; letter-spacing: 8px; }
  .card--back .wordmark__suffix { font-size: 20px; letter-spacing: 14px; }

  /* product mark */
  .product {
    position: absolute;
    right: 26px;
    top: 24px;
    text-align: right;
    font-family: "Tinos", serif;
  }
  .product__name {
    display: flex;
    align-items: center;
    justify-content: flex-end;
    gap: 6px;
    font-size: 20px;
    font-weight: 700;
    color: var(--ink);
  }
  .product__dot {
    width: 12px; height: 12px; border-radius: 50%;
    background: var(--ink);
  }
  .product__tag {
    margin-top: 4px;
    font-size: 13px;
    line-height: 1.25;
    color: var(--ink-soft);
  }

  /* contact */
  .person {
    position: absolute;
    left: 34px;
    top: 140px;
  }
  .person__name { font-size: 19px; font-weight: 700; letter-spacing: 0.5px; }
  .person__role { font-size: 14px; color: var(--ink-soft); }
  .contact {
    position: absolute;
    left: 34px;
    top: 196px;
    font-size: 14px;
    line-height: 1.35;
  }
  .contact__row { display: flex; align-items: center; gap: 6px; }
  .contact__icon {
    width: 14px; height: 14px; border-radius: 2px;
    background: var(--icon);
    display: inline-flex; align-items: center; justify-content: center;
  }
</style>
</head>
<body>

  <section class="card card--front" aria-label="Business card front">
    <div class="wordmark">
      <div class="wordmark__name">PEVRANOX</div>
      <div class="wordmark__suffix"><span class="wordmark__dots"></span>LLC<span class="wordmark__dots"></span></div>
    </div>

    <div class="product">
      <div class="product__name"><span class="product__dot"></span>Ember Ridge</div>
      <div class="product__tag">coolers<br>ember ridge</div>
    </div>

    <div class="person">
      <div class="person__name">DALE MORROW</div>
      <div class="person__role">Manager</div>
    </div>

    <div class="contact">
      <div>418 Mesa Trail, Ste 2</div>
      <div>Cedar Hollow, Texas 7720</div>
      <div class="contact__row">
        <span class="contact__icon">
          <svg width="9" height="9" viewBox="0 0 10 10" aria-hidden="true"><path d="M2 1l2 2-1 1.2c.6 1.2 1.6 2.2 2.8 2.8L7 6l2 2-1.3 1.3C4.5 9 1 5.5.7 2.3z" fill="#fff"/></svg>
        </span>512 555 0147
      </div>
      <div class="contact__row">
        <span class="contact__icon">
          <svg width="9" height="9" viewBox="0 0 10 10" aria-hidden="true"><rect x="1" y="2" width="8" height="6" fill="none" stroke="#fff" stroke-width="1.2"/><path d="M1 2l4 3 4-3" fill="none" stroke="#fff" stroke-width="1.2"/></svg>
        </span>dale@pevranox.com
      </div>
      <div class="contact__row">
        <span class="contact__icon">
          <svg width="9" height="9" viewBox="0 0 10 10" aria-hidden="true"><circle cx="5" cy="5" r="4" fill="none" stroke="#fff" stroke-width="1.1"/><path d="M1 5h8M5 1c-2 2.5-2 5.5 0 8M5 1c2 2.5 2 5.5 0 8" fill="none" stroke="#fff" stroke-width="0.9"/></svg>
        </span>www.pevranox.com
      </div>
    </div>
  </section>

  <section class="card card--back" aria-label="Business card back">
    <div class="wordmark">
      <div class="wordmark__name">PEVRANOX</div>
      <div class="wordmark__suffix"><span class="wordmark__dots"></span>LLC<span class="wordmark__dots"></span></div>
    </div>
  </section>

</body>
</html>
```